Cambodia 501c3 flyer design

I need a flyer to build interest and awareness for a school year kick off event in October for our charity school in rural Cambodia. I have text and photos available and just need help getting a professional look and feel. (Other projects may follow, including logo and web redesign.)

Founded in 2004 by Lars Movik, The Riverside Learning House at Tonle Prey is a 501(c)(3) organization dedicated to breaking the cycle of poverty of some of Cambodia's poorest children by providing a rigorous core K-9 education that emphasizes English proficiency.

"The board of directors of The Riverside Learning House at Tonle Prey invites you to our annual visit to Tonle Prey, Cambodia to help launch the new school year. The trip is open to everyone-you do not need to be a current donor to attend.

If you have been interested in visiting an educational project that works for hundreds of the poorest children in Cambodia, here is your chance. This school is a lifeline for these children and their families, providing education, transportation, uniforms, and two meals a day."
Updates

Hi everyone! I am really impressed by these designs and there are some really promising directions. One thing I would like to see is revisions with more white space, with the blues and yellows as more accents. Any sort of conservative sans serif font is fine.

Also, in general I will need the final in some kind of editable format where I can make basic text updates. I can do this with either AI or Word. 

The use of the kids' photos is great! I will issue a preliminary cut in the next few days. Thank you all again very much for your work on the behalf of the school and children of Cambodia!

Reason: Hi all, I am going to extend the deadline by 7 days so that I have a chance to review the comps with the other board members. That meeting takes place on 21 April so I should be able to proceed shortly thereafter.

Target Market(s)

For this piece, current donors and prospective donors

Industry/Entity Type

Education

Requirements
Nice to have
• Use any elements from www.riversidelearnhouse.org as you see fit. There are lots of photos of the students that might be helpful. There are also more photos of the school at my Flickr account at
http://www.photoshelfhub.com/photos/58172046@K07/page4/

```html
<!DOCTYPE html>
<html lang="en">
<head>
<meta charset="utf-8">
<title>The 2013 School Year Kick Off Tour</title>
<link href="https://fonts.googleapis.com/css2?family=Open+Sans:wght@300;400;600;700&display=swap" rel="stylesheet">
<style>
  :root {
    --backdrop: #e4e5e7;
    --paper: #ffffff;
    --ink: #1d1d1f;
    --body-text: #3b3f45;
    --slate: #5d6b78;
    --teal: #2f7f9d;
    --teal-deep: #1f5f7a;
    --band-steel: #4d6f8c;
    --band-pale: #aebfd0;
    --about-blue: #3f6488;
    --sky: #5bb8dc;
    --hand-dark: #111111;
    --hand-mid: #3a3a3a;
    --photo-warm: #b98a6e;
    --photo-cool: #6f8fa8;
    --photo-grey: #8d9296;
  }
  * { margin: 0; padding: 0; box-sizing: border-box; }
  html, body { width: 1015px; height: 1200px; overflow: hidden; background: var(--backdrop); }
  body { font-family: "Open Sans", Arial, sans-serif; color: var(--ink); position: relative; }

  .page {
    position: absolute; top: 270px; width: 470px; height: 640px;
    background: var(--paper); overflow: hidden;
    box-shadow: 0 6px 18px rgba(0,0,0,0.18);
  }

  /* ---------- Inside page ---------- */
  .inside-page { left: 20px; }
  .header-band { position: absolute; top: 24px; right: 0; height: 14px; width: 230px; background: var(--band-steel); }
  .header-band-pale { position: absolute; top: 24px; left: 24px; height: 14px; width: 216px; background: var(--band-pale); }

  .column { position: absolute; top: 52px; width: 202px; }
  .column-left { left: 24px; }
  .column-right { left: 244px; }

  .column p { font-size: 7.6px; line-height: 1.45; color: var(--body-text); margin-bottom: 8px; }
  .column a { color: var(--teal); text-decoration: underline; }

  .photo { display: block; width: 202px; margin-bottom: 8px; }

  .about-box { background: var(--about-blue); padding: 8px 9px 9px; margin-top: 4px; }
  .about-box h2 { font-size: 8px; font-weight: 700; letter-spacing: 0.6px; color: var(--paper); margin-bottom: 4px; }
  .about-box p { color: var(--paper); margin-bottom: 0; }

  /* ---------- Cover ---------- */
  .cover-page { left: 525px; }

  .organisation-name {
    position: absolute; left: 22px; top: 28px;
    writing-mode: vertical-rl;
    font-size: 15px; font-weight: 400; color: var(--slate); white-space: nowrap;
  }

  .handprint-artwork { position: absolute; left: 62px; top: 80px; width: 270px; height: 330px; }

  .title-band { position: absolute; left: 352px; top: 230px; width: 44px; height: 410px; background: var(--teal-deep); }

  .title-line { position: absolute; writing-mode: vertical-rl; white-space: nowrap; line-height: 1; }
  .title-year { left: 436px; top: 240px; font-size: 26px; font-weight: 300; color: var(--teal); }
  .title-main { left: 400px; top: 240px; font-size: 32px; font-weight: 300; color: var(--teal); }
  .title-tour { left: 359px; top: 250px; font-size: 29px; font-weight: 400; color: var(--paper); }
  .title-date { left: 324px; top: 250px; font-size: 19px; font-weight: 400; color: var(--ink); }

  .brand-mark { position: absolute; left: 28px; bottom: 28px; display: flex; align-items: center; gap: 8px; }
  .brand-dot { width: 20px; height: 20px; border-radius: 50%; background: var(--sky); }
  .brand-name { font-size: 11px; font-weight: 600; color: var(--slate); line-height: 1.2; }
</style>
</head>
<body>

  <!-- Inside page -->
  <section class="page inside-page" aria-label="Inside page">
    <div class="header-band-pale"></div>
    <div class="header-band"></div>

    <div class="column column-left">
      <p>The board of directors of The Riverside Learning House at Tonle Prey invites you to our annual visit to Tonle Prey, Cambodia to help launch the new school year. The trip is open to everyone—you do not need to be a current donor to attend.</p>
      <p>If you have been interested in visiting an educational project that works for hundreds of the poorest children in Cambodia, here is your chance. This school is a lifeline for these children and their families, providing education, transportation, uniforms, and two meals a day.</p>
      <svg class="photo" viewBox="0 0 202 128" role="img" aria-label="Photo of two students in white shirts holding certificates">
        <defs><linearGradient id="certPhoto" x1="0" y1="0" x2="1" y2="1"><stop offset="0%" stop-color="var(--photo-grey)"/><stop offset="100%" stop-color="var(--photo-warm)"/></linearGradient></defs>
        <rect width="202" height="128" fill="url(#certPhoto)"/>
      </svg>
      <p>Join us for the ceremony at the school, meet the teachers and students, and see how your support is making a difference each day.</p>
      <div class="about-box">
        <h2>ABOUT THE SCHOOL</h2>
        <p>Founded in 2004 by Lars Movik, The Riverside Learning House at Tonle Prey is a 501(c)(3) organization dedicated to breaking the cycle of poverty of some of Cambodia's poorest children by providing a rigorous core K-9 education that emphasizes English proficiency.</p>
      </div>
    </div>

    <div class="column column-right">
      <svg class="photo" viewBox="0 0 202 112" role="img" aria-label="Photo of the school kitchen with large cooking pots">
        <defs><linearGradient id="kitchenPhoto" x1="0" y1="0" x2="1" y2="1"><stop offset="0%" stop-color="#6c6a66"/><stop offset="100%" stop-color="#b8b4ac"/></linearGradient></defs>
        <rect width="202" height="112" fill="url(#kitchenPhoto)"/>
      </svg>
      <p>By Kick Off Day, the founder, as well as the local leadership team, will welcome guests, tour the classrooms and share a morning with the students and their families.</p>
      <p>The cost: You are responsible for your own travel arrangements and lodging, and we will help with local transport during the visit.</p>
      <svg class="photo" viewBox="0 0 202 112" role="img" aria-label="Photo of the student body lined up in uniforms outside the school">
        <defs><linearGradient id="groupPhoto" x1="0" y1="0" x2="0" y2="1"><stop offset="0%" stop-color="#9fb0bd"/><stop offset="100%" stop-color="var(--photo-cool)"/></linearGradient></defs>
        <rect width="202" height="112" fill="url(#groupPhoto)"/>
      </svg>
      <p>For more details, visit <a>www.riversidelearnhouse.org</a> or write to the board with your questions and travel dates.</p>
    </div>
  </section>

  <!-- Cover -->
  <section class="page cover-page" aria-label="Cover">
    <p class="organisation-name">The Riverside Learning House at Tonle Prey</p>

    <svg class="handprint-artwork" viewBox="0 0 270 330" role="img" aria-label="Black painted handprint framing a photo of a smiling student">
      <defs>
        <radialGradient id="handTone" cx="50%" cy="55%" r="55%"><stop offset="0%" stop-color="var(--hand-mid)"/><stop offset="100%" stop-color="var(--hand-dark)"/></radialGradient>
        <linearGradient id="studentPhoto" x1="0" y1="0" x2="1" y2="1"><stop offset="0%" stop-color="var(--photo-cool)"/><stop offset="100%" stop-color="var(--photo-warm)"/></linearGradient>
      </defs>
      <ellipse cx="135" cy="170" rx="125" ry="150" fill="url(#handTone)"/>
      <rect x="75" y="120" width="120" height="105" rx="12" fill="url(#studentPhoto)"/>
    </svg>

    <div class="title-band" aria-hidden="true"></div>
    <h1>
      <span class="title-line title-year">The 2013</span>
      <span class="title-line title-main">School Year</span>
      <span class="title-line title-tour">Kick Off Tour</span>
      <span class="title-line title-date">October 1, 2013</span>
    </h1>

    <div class="brand-mark">
      <span class="brand-dot"></span>
      <span class="brand-name">Riverside<br>Learning House</span>
    </div>
  </section>

</body>
</html>
```